Loopnest Ad Image for Ebook

I need someone to design a good looking loopnest ad image for my ebook. Must comply with Loopnest ad police and generate lots of clicks and opt ins. Use my 3d cover attached.

```html
<!DOCTYPE html>
<html lang="en">
<head>
<meta charset="utf-8">
<title>The Smart Writing Roadmap – Loopnest Ad</title>
<link href="https://fonts.googleapis.com/css2?family=Poppins:wght@700;800&display=swap" rel="stylesheet">
<style>
  :root {
    --ink: #111111;
    --brand-blue: #1b9be3;
    --navy: #0e2a47;
    --paper: #ffffff;
    --cover-dark: #141414;
    --cover-light: #e9edf1;
  }
  html, body {
    margin: 0;
    padding: 0;
    overflow: hidden;
    background: var(--paper);
  }
  .ad {
    position: relative;
    width: 1200px;
    height: 682px;
    overflow: hidden;
    background: var(--paper);
    font-family: "Poppins", sans-serif;
  }
  .accent-bands {
    position: absolute;
    left: 0;
    top: 0;
    width: 1200px;
    height: 682px;
  }
  .headline {
    position: absolute;
    left: 98px;
    top: 128px;
    margin: 0;
    font-weight: 800;
    font-size: 76px;
    line-height: 100px;
    letter-spacing: -1px;
    color: var(--ink);
  }
  .headline__line { display: block; }
  .headline__line--accent { color: var(--brand-blue); }
  .ebook-cover {
    position: absolute;
    left: 690px;
    top: 30px;
    width: 330px;
    height: 596px;
    background: linear-gradient(165deg, var(--cover-light) 0%, #c9d2db 42%, var(--cover-dark) 62%, var(--cover-dark) 100%);
    box-shadow: 10px 14px 24px rgba(0, 0, 0, 0.25);
  }
  .brand-tag {
    position: absolute;
    left: 58px;
    top: 498px;
    width: 372px;
    height: 142px;
    background: var(--paper);
    transform: rotate(-2.5deg);
    display: flex;
    align-items: center;
    justify-content: center;
    gap: 16px;
  }
  .brand-tag__mark {
    width: 34px;
    height: 34px;
    background: var(--brand-blue);
  }
  .brand-tag__name {
    font-weight: 800;
    font-size: 34px;
    color: var(--navy);
    white-space: nowrap;
  }
</style>
</head>
<body>
  <main class="ad">
    <svg class="accent-bands" viewBox="0 0 1200 682" aria-hidden="true">
      <rect x="430" y="532" width="770" height="36" fill="var(--ink)"/>
      <path d="M500 568 H1200 V662 H470 Q452 662 458 646 Z" fill="var(--brand-blue)"/>
    </svg>

    <h1 class="headline">
      <span class="headline__line">The Smart</span>
      <span class="headline__line">Writing</span>
      <span class="headline__line headline__line--accent">Roadmap</span>
    </h1>

    <div class="ebook-cover" role="img" aria-label="3D ebook cover of The Smart Writing Roadmap with a photo of hands typing on a laptop showing a blog"></div>

    <div class="brand-tag">
      <span class="brand-tag__mark"></span>
      <span class="brand-tag__name">Writing with Nora</span>
    </div>
  </main>
</body>
</html>
```